A weight loss and fitness website design

I am into different types of modern weight loss techniques for people who are a little fatty and wish to be physically and mentally fit. Basically, the website is to teach people how to reduce weight using different methods such as diet, exercises, yoga and other forms. I would need an eye catching website which would make visitors want to come back. The will be also be different forms of exercises for a health and fit life. This said, my website is to have two categories of
1) weight loss techniques
2) exercise of fit and healthy living.
I prefer bright colors such as green, blue, yellow, and orange. Imagery should include before and after pictures of people suffering from obesity, people under going exercises.
Designers can get ideas and inspiration from the website fyrnexa.com which i was previously part of the team.
Target Market(s)
My target audience are people suffering from obesity, malnutrition and physical deficiency.
Industry/Entity Type
Fitness
Coding
Number of Pages Required
1 page
Look and feel

```html
<!DOCTYPE html>
<html lang="en">
<head>
<meta charset="utf-8">
<title>Velora Fitness</title>
<link rel="stylesheet" href="https://fonts.googleapis.com/css2?family=Oswald:wght@300;400;500;600&display=swap">
<style>
:root{
  --yellow:#f2f20a;
  --green:#1f7d00;
  --blue:#0a0a82;
  --orange:#ff5a00;
  --dark:#2f2f2f;
  --darker:#1e1e1e;
  --white:#ffffff;
  --ink:#111111;
  --accent:#e8790a;
  --link-green:#7fd34a;
}
*{margin:0;padding:0;box-sizing:border-box}
html,body{width:1200px;height:3351px;overflow:hidden}
body{font-family:"Oswald",sans-serif;color:var(--white);position:relative;background:var(--white)}
.abs{position:absolute}
.ph{position:absolute}

/* header */
.site-header{position:absolute;left:0;top:0;width:1200px;height:84px;background:var(--yellow)}
.brand{position:absolute;left:130px;top:25px;display:flex;align-items:center;gap:8px;font-size:23px;font-weight:600;color:var(--accent)}
.brand-dot{width:22px;height:22px;border-radius:50%;background:var(--accent)}
.main-nav{position:absolute;top:33px;left:478px;display:flex;gap:24px;font-size:13.5px;font-weight:500;color:var(--ink)}
.main-nav .current{color:var(--accent)}
.search{position:absolute;left:1063px;top:33px}

/* hero */
.hero{position:absolute;left:0;top:84px;width:1200px;height:476px;background:linear-gradient(90deg,#1a1a1a 0%,#262626 55%,#303030 100%)}
.hero-photo{left:740px;top:0;width:360px;height:476px;background:linear-gradient(180deg,#8c6a55 0%,#7a5a46 50%,#2f3a55 100%)}
.hero-title{position:absolute;left:247px;top:140px;font-size:50px;font-weight:300;line-height:96px}

/* cta */
.cta-band{position:absolute;left:0;top:560px;width:1200px;height:98px;background:var(--yellow);color:var(--ink)}
.cta-text{position:absolute;left:121px;top:31px;font-size:25px;font-weight:500}
.cta-button{position:absolute;left:795px;top:23px;width:140px;height:52px;border:2px solid var(--ink);display:flex;align-items:center;justify-content:center;font-size:21px;font-weight:500}

/* welcome */
.welcome{position:absolute;left:0;top:658px;width:1200px;height:467px;background:var(--green)}
.welcome-photo-1{left:121px;top:73px;width:199px;height:314px;background:linear-gradient(180deg,#d9d2cc 0%,#c6a58e 45%,#2a2a2a 100%)}
.welcome-photo-2{left:373px;top:73px;width:201px;height:314px;background:linear-gradient(180deg,#cfcfcf 0%,#b8927a 45%,#3a3a3a 100%)}
.welcome-title{position:absolute;left:626px;top:80px;font-size:38px;font-weight:400}
.welcome-text{position:absolute;left:626px;top:146px;width:436px;font-size:18px;line-height:30.5px;font-weight:400}

/* weight loss */
.techniques{position:absolute;left:0;top:1125px;width:1200px;height:738px;background:var(--blue)}
.section-h{font-size:34px;font-weight:400;line-height:1.2}
.body-text{font-size:17.5px;line-height:30.5px;font-weight:400}
.tech-col{position:absolute;left:121px;width:452px}
.person-frame{background:linear-gradient(180deg,#ffffff 0%,#ffffff 20%,#e8d6c8 24%,#1e1e1e 40%,#2a2a2a 92%,#ffffff 96%)}
.photo-label{position:absolute;font-size:20px;width:201px;text-align:center}

/* nutrition */
.nutrition{position:absolute;left:0;top:1863px;width:1200px;height:1122px;background:var(--orange)}
.nut-h{font-size:30px;font-weight:400}
.nut-text{font-size:16.5px;line-height:30px;font-weight:400}

/* testimonial */
.testimonial{position:absolute;left:0;top:2985px;width:1200px;height:252px;background:linear-gradient(90deg,#6e6e70,#8e8e92 50%,#6a6a6c)}
.quote-box{position:absolute;left:200px;top:76px;width:881px;height:106px;background:rgba(150,150,154,.55)}
.avatar{position:absolute;left:121px;top:98px;width:80px;height:80px;border-radius:50%;background:linear-gradient(180deg,#4a3a30,#b58a70)}
.quote-text{position:absolute;left:26px;top:18px;font-size:16px;font-weight:400}
.quote-name{position:absolute;left:26px;top:62px;font-size:16px;font-weight:500}
.quote-mark{position:absolute;left:585px;top:57px;width:30px;height:30px;border-radius:50%;border:2px solid var(--white);display:flex;align-items:center;justify-content:center;font-size:24px;line-height:1;padding-top:10px}

/* footer */
.footer-nav{position:absolute;left:0;top:3237px;width:1200px;height:55px;background:var(--dark);display:flex;justify-content:center;align-items:center;gap:26px;font-size:13px;font-weight:500;color:var(--link-green)}
.footer-bar{position:absolute;left:0;top:3292px;width:1200px;height:59px;background:var(--darker)}
.copyright{position:absolute;left:121px;top:18px;font-size:15px;font-weight:400}
.social{position:absolute;left:920px;top:21px;display:flex;gap:26px}
.social span{width:18px;height:18px;border-radius:50%;background:#2a7cc7}
.social span.warm{background:#e88b0a}
</style>
</head>
<body>

<header class="site-header">
  <div class="brand"><span class="brand-dot"></span>Velora Fitness</div>
  <nav class="main-nav">
    <span class="current">HOME</span>
    <span>About Us</span>
    <span>Weight loss techniques</span>
    <span>Exercise of fit and healthy living</span>
    <span>Contact Us</span>
  </nav>
  <svg class="search" width="16" height="18" viewBox="0 0 16 18"><circle cx="6.5" cy="6.5" r="5" fill="none" stroke="#e8790a" stroke-width="1.8"/><line x1="10" y1="10.5" x2="14.5" y2="16" stroke="#e8790a" stroke-width="1.8"/></svg>
</header>

<section class="hero">
  <div class="ph hero-photo" role="img" aria-label="Athletic man training on gymnastic rings"></div>
  <h1 class="hero-title">Discover the power of<br>Velora Fitness Training</h1>
</section>

<section class="cta-band">
  <p class="cta-text">Start a personal training session with one of our fitness trainers</p>
  <div class="cta-button">Get Started</div>
</section>

<section class="welcome">
  <div class="ph welcome-photo-1" role="img" aria-label="Woman in sportswear flexing with a measuring tape"></div>
  <div class="ph welcome-photo-2" role="img" aria-label="Smiling woman holding a jump rope"></div>
  <h2 class="welcome-title">Welcome</h2>
  <p class="welcome-text">Ut enim ad minim veniam, quis nostrud exercitation ullamco laboris nisi ut aliquip ex ea commodo consequat. Duis aute irure dolor in reprehenderit in voluptate velit esse cillum dolore eu fugiat nulla pariatur. Excepteur sint occaecat cupidatat non proident, sunt in culpa qui officia deserunt mollit anim id est laborum. Duis aute irure dolor in reprehenderit in voluptate velit esse cillum dolore eu fugiat nulla pariatur.</p>
</section>

<section class="techniques">
  <div class="tech-col" style="top:82px">
    <h2 class="section-h">Our Weight Loss Techniques</h2>
    <p class="body-text" style="margin-top:10px">Lorem Ipsum is simply dummy text of the printing and typesetting industry. Lorem Ipsum has been the industry's standard dummy text ever since the 1500s, when an unknown printer took a galley of type and scrambled it to make a type specimen book. It has survived not only five centuries, but also the leap into electronic typesetting, remaining essentially unchanged.</p>
    <h2 class="section-h" style="margin-top:18px">Reach your goals faster</h2>
    <p class="body-text" style="margin-top:10px">Whether you simply want to lose fat, gain muscle or be healthy - or you want to work on a specific sport or combination of goals - Velora will tailor your workouts to accommodate. Velora will work with you to find an appropriate training volume, intensity, and frequency, and will select exercises and progressions to get you where you're going efficiently. Why drive half the speed limit?</p>
  </div>
  <div class="tech-col" style="left:626px;top:82px">
    <h2 class="section-h">Personalize your Exercise</h2>
    <p class="body-text" style="margin-top:10px;font-size:16px">We adapts your workouts to you, your goals, and your progress.</p>
  </div>
  <div class="ph person-frame" style="left:626px;top:230px;width:201px;height:357px" role="img" aria-label="Woman before weight loss"></div>
  <div class="ph person-frame" style="left:880px;top:230px;width:201px;height:357px" role="img" aria-label="Woman after weight loss"></div>
  <div class="photo-label" style="left:626px;top:618px">Before</div>
  <div class="photo-label" style="left:880px;top:618px">After</div>
</section>

<section class="nutrition">
  <h2 class="abs section-h" style="left:121px;top:78px;font-size:38px">Track &amp; Optimize Nutrition</h2>
  <p class="abs nut-text" style="left:121px;top:146px">Robust food tracking and recommendations to help you reach any goal.</p>

  <h3 class="abs nut-h" style="left:121px;top:230px">Eat smarter</h3>
  <p class="abs nut-text" style="left:121px;top:282px;width:620px">All of your nutrition targets are tailored to your specific goals and body. The nutrition requirements of gaining muscle, improving health, or optimizing athletic performance are all very different, and Velora will recommend both macro and micronutrient targets accordingly.</p>
  <div class="ph" style="left:795px;top:224px;width:286px;height:160px;background:#151515" role="img" aria-label="Fruit salad calorie calculator screen"></div>

  <div class="ph" style="left:121px;top:434px;width:284px;height:160px;background:linear-gradient(135deg,#1f2d4a,#d89a30 55%,#243152)" role="img" aria-label="Woman lifting dumbbells"></div>
  <h3 class="abs nut-h" style="left:457px;top:436px">Your targets update with your workouts</h3>
  <p class="abs nut-text" style="left:457px;top:494px;width:624px">Complete a great workout? Need to refuel for next time? We'll help you consume enough carbohydrate to replenish muscle glycogen. Missed your planned session? No problem, we'll adjust your calories and other targets as necessary.</p>

  <h3 class="abs nut-h" style="left:121px;top:646px">Track your meals seamlessly</h3>
  <p class="abs nut-text" style="left:121px;top:700px;width:620px">Velora instantly remembers your tracked foods and meals. Record a frequently eaten meal with a single click, and reap the rewards of nutrition tracking faster and easier.</p>
  <div class="ph" style="left:795px;top:642px;width:286px;height:142px;background:linear-gradient(90deg,#f2efe8,#e6c2a0 50%,#c8d4a8)" role="img" aria-label="Chart of foods grouped by type"></div>

  <div class="ph" style="left:121px;top:834px;width:286px;height:213px;background:linear-gradient(180deg,#ffffff,#eef3e6);border:3px solid #cfd8e0" role="img" aria-label="Recommended foods cards with vegetables, nuts and fish"></div>
  <h3 class="abs nut-h" style="left:457px;top:832px">Remove uncertainty with recommended foods</h3>
  <p class="abs nut-text" style="left:457px;top:890px;width:624px">Based on your progress towards your nutrient targets, Velora will recommend foods to help you fill deficiencies. Need to hit your protein and omega-3 fatty acid targets? Consider salmon or scallops. Looking for healthy fats and fiber? Give walnuts or almonds a look. No guesswork required, we'll surface a list of foods that best meet your needs.</p>
</section>

<section class="testimonial" role="img" aria-label="Gym interior in muted grey">
  <div class="quote-mark">&#8221;</div>
  <div class="quote-box">
    <p class="quote-text">This application tops any other workout app and not only beats them but totally blows them out of the water</p>
    <p class="quote-name">Marcus Lindell</p>
  </div>
  <div class="avatar" role="img" aria-label="Portrait of the reviewer"></div>
</section>

<nav class="footer-nav">
  <span>HOME</span>
  <span>About Us</span>
  <span>Weight loss techniques</span>
  <span>Exercise of fit and healthy living</span>
  <span>Contact Us</span>
</nav>

<footer class="footer-bar">
  <p class="copyright">© 2016 - Velora Fitness - All rights reserved</p>
  <div class="social"><span></span><span></span><span></span><span class="warm"></span></div>
</footer>

</body>
</html>
```